Business Card Design to Compliment attached Letterhead

I am looking for a really nice business card for my new business launch. I develop Excel based applications to support administrative and operational processes. I have attached my letterhead so you have an idea what the components should look like. I tried uploading the various components into the "Design your own" section, but they looked really rough, so I am looking for someone to be able to come up with a nice crisp version of the tetras square and the Company Name styling that will compliment my letterhead; and then put all of this into a business card design that is crisp, clean and professional looking. I am considering using spot gloss, because I think it will add an extra touch of class.

Industry/Entity Type

Business

Contact Information for Business Card

Pendrix Consulting, Tabula Remedies for Weekday Puzzles, Mirela Dunstan, Business Systems Analyst, Tabula Specialist, 0438 270 915, mirela@pendrixconsulting.com.au www.pendrixconsulting.com.au

Requirements
Must have
• I want to use the same colors as the attached file and keep the fonts used for "Pendrix" and "Consulting"
• I need the Tetras square to be re-created. I did it myself using photoshop and it is pretty rough. I need it to be crisp and clean and professional looking.
• Please include my name, title, phone, email, web address and "Tabula Remedies to Weekday Puzzles"
Nice to have
• So far I have liked the designs that are a little bit different. I want people to look at my card and say "Nice Card"
Should not have
• I don't like the see-through format.
• Do not include any information about Quorra Ventures or the address
• Please dont use my version of the tetras square, it is fuzzy and poorly drawn (I did it myself), I need it to be crisp, and clean otherwise it will spoil the effect of my nice new cards.

```html
<!DOCTYPE html>
<html lang="en">
<head>
<meta charset="utf-8">
<title>Pendrix Consulting — Business Card</title>
<link href="https://fonts.googleapis.com/css2?family=Open+Sans:wght@400;600;700&display=swap" rel="stylesheet">
<style>
  :root {
    --backdrop: #e7e4e1;
    --card-light: #f4f5f7;
    --card-purple: #5a2174;
    --card-purple-bright: #62268a;
    --accent-blue: #1a7fb4;
    --brand-purple: #6a2a8e;
    --text-warm: #dcc5b2;
    --text-warm-soft: #cdb3a3;
    --icon-cut: #5a2174;
  }
  * { margin: 0; padding: 0; box-sizing: border-box; }
  html, body {
    width: 1200px;
    height: 970px;
    overflow: hidden;
    background: var(--backdrop);
  }
  .canvas {
    position: relative;
    width: 1200px;
    height: 970px;
  }
  .business-card {
    position: absolute;
    left: 172px;
    top: 270px;
    width: 856px;
    height: 475px;
    background: var(--card-light);
    overflow: hidden;
    box-shadow: 0 18px 40px rgba(0,0,0,0.18);
    font-family: "Open Sans", Arial, sans-serif;
  }
  .card-wave {
    position: absolute;
    inset: 0;
    width: 856px;
    height: 475px;
  }
  .brand {
    position: absolute;
    left: 44px;
    top: 202px;
    display: flex;
    align-items: center;
    gap: 12px;
  }
  .brand-square {
    width: 34px;
    height: 34px;
    background: var(--brand-purple);
  }
  .brand-name {
    font-size: 26px;
    font-weight: 700;
    color: var(--brand-purple);
    white-space: nowrap;
  }
  .holder {
    position: absolute;
    left: 453px;
    top: 86px;
    color: var(--text-warm);
  }
  .holder-name {
    font-size: 22px;
    font-weight: 700;
    margin-bottom: 4px;
  }
  .holder-role {
    font-size: 17px;
    font-weight: 400;
    line-height: 26px;
    color: var(--text-warm-soft);
  }
  .contact-list {
    position: absolute;
    left: 453px;
    top: 272px;
    list-style: none;
    color: var(--text-warm);
  }
  .contact-item {
    display: flex;
    align-items: center;
    height: 28px;
    font-size: 18px;
  }
  .contact-icon {
    width: 16px;
    height: 16px;
    margin-right: 25px;
    fill: var(--text-warm);
  }
  .tagline {
    position: absolute;
    left: 453px;
    top: 360px;
    font-size: 18px;
    color: var(--text-warm-soft);
  }
</style>
</head>
<body>
<main class="canvas">
  <section class="business-card">
    <svg class="card-wave" viewBox="0 0 856 475" aria-hidden="true">
      <defs>
        <linearGradient id="purpleFade" x1="0" y1="0" x2="1" y2="0">
          <stop offset="0" stop-color="var(--card-purple)"/>
          <stop offset="1" stop-color="var(--card-purple-bright)"/>
        </linearGradient>
      </defs>
      <path d="M360 0 C 395 110, 405 170, 395 260 C 385 350, 360 420, 345 475 L 856 475 L 856 0 Z" fill="var(--accent-blue)"/>
      <path d="M370 0 C 408 110, 418 170, 408 260 C 398 350, 373 420, 358 475 L 856 475 L 856 0 Z" fill="url(#purpleFade)"/>
    </svg>

    <div class="brand">
      <span class="brand-square"></span>
      <span class="brand-name">Pendrix Consulting</span>
    </div>

    <div class="holder">
      <p class="holder-name">Mirela Dunstan</p>
      <p class="holder-role">Business Systems Analyst</p>
      <p class="holder-role">Tabula Specialist</p>
    </div>

    <ul class="contact-list">
      <li class="contact-item">
        <svg class="contact-icon" viewBox="0 0 16 16" aria-hidden="true"><path d="M2 5 C2 3 4 2 8 2 C12 2 14 3 14 5 L11 6 L10 4.5 C9 4.2 7 4.2 6 4.5 L5 6 Z M4 7 L12 7 L14 13 L2 13 Z"/></svg>
        0438 270 915
      </li>
      <li class="contact-item">
        <svg class="contact-icon" viewBox="0 0 16 16" aria-hidden="true"><path d="M1 3 L15 3 L15 13 L1 13 Z M2 4 L8 9 L14 4" stroke="var(--icon-cut)" stroke-width="1"/></svg>
        mirela@pendrixconsulting.com.au
      </li>
      <li class="contact-item">
        <svg class="contact-icon" viewBox="0 0 16 16" aria-hidden="true"><circle cx="8" cy="8" r="7"/><path d="M1 8 H15 M8 1 V15 M3 4 H13 M3 12 H13" stroke="var(--icon-cut)" stroke-width="0.9" fill="none"/><ellipse cx="8" cy="8" rx="3" ry="7" stroke="var(--icon-cut)" stroke-width="0.9" fill="none"/></svg>
        www.pendrixconsulting.com.au
      </li>
    </ul>

    <p class="tagline">Tabula Remedies for Weekday Puzzles</p>
  </section>
</main>
</body>
</html>
```